Trifold - Harbor Lantern Therapy

Maren Holloway, Psy.D.Licensed Psychologist

this is for hypnosis and meditation
I like decorative font for my name (conservative decorative)

calming effect is most imortant

Target Market(s)

clients with depression, pain, anxiety - adults and aged

Industry/Entity Type

Conservative

Font styles to use
Serif

Colors
abd037
85cae6
cadf82
34a7d7
ffffff
886aae
6b449b

Requirements
Must have
• I like zen-like calming effects. lime Green, light blues and purple. I like waves and color.
• I like water and light, flowers and plants - bamboo, stacking rocks, ocean, water, lotus flowers
Should not have
• not too much purple
• Mostly green and blue

```html
<!DOCTYPE html>
<html lang="en">
<head>
<meta charset="utf-8">
<title>Trifold – Harbor Lantern Therapy</title>
<link href="https://fonts.googleapis.com/css2?family=Raleway:wght@300;400;600;700&family=Open+Sans:wght@400;600&family=Libre+Baskerville:wght@700&family=Great+Vibes&display=swap" rel="stylesheet">
<style>
:root{
  --lime:#abd037;
  --green:#7db43a;
  --leaf:#cadf82;
  --sky:#85cae6;
  --blue:#34a7d7;
  --mist:#c4e7f6;
  --lilac:#886aae;
  --purple:#6b449b;
  --ink:#3d3d3d;
  --paper:#ffffff;
  --stage:#eef1f3;
}
*{box-sizing:border-box;margin:0;padding:0}
html,body{width:1200px;height:1200px;overflow:hidden;background:var(--stage)}
body{font-family:"Open Sans",Arial,sans-serif;color:var(--ink)}
.spread{position:absolute;left:30px;width:1140px;height:560px;display:flex;box-shadow:0 4px 18px rgba(0,0,0,.15)}
.spread--outside{top:25px}
.spread--inside{top:615px}
.panel{position:relative;width:380px;height:560px;background:var(--paper);overflow:hidden}
.panel + .panel{border-left:1px solid #e6e6e6}
.art{position:absolute;left:0;width:100%}
.brand{display:flex;align-items:center;justify-content:center;gap:8px;font-family:"Raleway",sans-serif;font-weight:600;letter-spacing:4px;color:var(--green);font-size:17px}
.brand__dot{width:16px;height:16px;border-radius:50%;background:var(--green)}
.doc-name{font-family:"Raleway",sans-serif;font-weight:300;font-size:19px;color:var(--purple);text-align:center}
.script{font-family:"Great Vibes",cursive;font-size:26px;color:var(--blue);text-align:center}
.pill{display:inline-flex;align-items:center;gap:6px;background:var(--blue);color:#fff;font-family:"Raleway",sans-serif;font-weight:700;font-size:16px;padding:4px 16px;border-radius:16px}
.url{font-family:"Raleway",sans-serif;letter-spacing:3px;font-size:11px;color:#fff;text-align:center}
/* services panel */
.services{position:absolute;top:22px;left:24px;right:22px;z-index:1}
.services__title{font-family:"Raleway",sans-serif;font-weight:700;color:var(--purple);font-size:15px;letter-spacing:.5px;border-bottom:2px solid var(--blue);padding-bottom:3px;margin-bottom:6px}
.service{margin-bottom:7px}
.service__label{display:inline-flex;align-items:center;gap:6px;background:var(--blue);color:#fff;font-family:"Raleway",sans-serif;font-weight:700;font-size:11px;padding:2px 10px 2px 3px;border-radius:10px;margin-bottom:3px}
.service__icon{width:13px;height:13px;border-radius:50%;background:#fff}
.service p{font-size:9.5px;line-height:1.35}
.fee{font-family:"Raleway",sans-serif;font-size:11px;color:var(--ink)}
.fee b{display:block;color:var(--blue);font-style:italic}
/* back panel */
.back{position:absolute;top:220px;left:0;right:0;text-align:center}
.back .doc-name{font-size:17px;margin-top:14px}
.back__role{font-family:"Raleway",sans-serif;font-weight:700;color:var(--purple);font-size:16px}
.back__motto{font-family:"Raleway",sans-serif;color:var(--blue);font-size:16px;line-height:1.25;margin-top:10px}
.contact{margin-top:20px;font-size:11px;line-height:1.35}
.contact__row{display:flex;flex-direction:column;align-items:center;margin-bottom:9px}
.contact svg{margin-bottom:2px}
/* cover */
.cover{position:absolute;top:275px;left:0;right:0;text-align:center}
.cover__head{font-family:"Libre Baskerville",Georgia,serif;color:var(--lime);font-size:19px;line-height:1.1;margin-top:4px}
.cover__head span{color:var(--purple)}
.cover__sub{font-family:"Raleway",sans-serif;font-size:13px;color:var(--ink);margin-top:6px}
.cover__spec{font-family:"Raleway",sans-serif;font-weight:700;color:var(--purple);font-size:15px;line-height:1.2}
/* inside */
.copy{position:absolute;left:22px;right:22px}
.h{font-family:"Raleway",sans-serif;font-weight:700;font-size:14px;color:var(--purple);margin-bottom:5px}
.h--ink{color:#2c2c2c}
.copy p{font-size:9.5px;line-height:1.4;margin-bottom:10px}
.ticks{list-style:none;font-size:10.5px;line-height:1.75}
.ticks li{display:flex;align-items:center;gap:7px}
.tick{width:11px;height:11px;border-radius:50%;background:var(--blue);flex:none;position:relative}
.tick::after{content:"";position:absolute;left:3px;top:2px;width:3px;height:5px;border:solid #fff;border-width:0 1.5px 1.5px 0;transform:rotate(45deg)}
.panel--mist{background:var(--mist)}
.bio-contact{position:absolute;top:200px;left:0;right:0;text-align:center}
.bio-phone{font-family:"Raleway",sans-serif;font-weight:700;color:var(--purple);font-size:20px;margin-top:10px}
.bio-url{font-family:"Raleway",sans-serif;letter-spacing:3px;font-size:11px;color:var(--blue)}
</style>
</head>
<body>

<!-- Outside spread -->
<section class="spread spread--outside">

  <article class="panel panel--services">
    <svg class="art" style="top:440px" width="380" height="120" viewBox="0 0 380 120" role="img" aria-label="Photo of bamboo stalks reflected in still green water">
      <defs><linearGradient id="bamboo" x1="0" y1="0" x2="1" y2="1"><stop offset="0" stop-color="#e9f5c8"/><stop offset=".5" stop-color="#9ccc4a"/><stop offset="1" stop-color="#3f7d22"/></linearGradient></defs>
      <path d="M0 40 Q170 -5 380 12 V120 H0Z" fill="url(#bamboo)"/>
      <path d="M0 40 Q170 -5 380 12" fill="none" stroke="var(--blue)" stroke-width="3"/>
    </svg>
    <div class="services">
      <h2 class="services__title">PSYCHOLOGICAL SERVICES</h2>
      <div class="service">
        <span class="service__label"><span class="service__icon"></span>Initial evaluation</span>
        <p>Mental health assessment, diagnosis and comprehensive wellness planning.</p>
      </div>
      <div class="service">
        <span class="service__label"><span class="service__icon"></span>Harbor Lantern Therapy (HLT)</span>
        <p>Resolve emotional distress, heartbreak and grief. HLT clears trauma at the subconscious level with gentle guided communication. The most troubling memories are worked through and clients gain a sense of clarity, peace and power. Only a couple of sessions are needed to experience dramatic and long-lasting effects.</p>
      </div>
      <div class="service">
        <span class="service__label"><span class="service__icon"></span>Eye Movement Desensitization &amp; Reprocessing</span>
        <p>Evidence-based treatment for post-traumatic stress disorder, anxiety, depression and adverse experiences. Experience relief and empowerment. More information at calmpath.org.</p>
      </div>
      <div class="service">
        <span class="service__label"><span class="service__icon"></span>Short-term talk therapy</span>
        <p>Psychotherapy to create a more satisfying life. Proactive approach to seeking effective solutions for your most pressing emotional and relational problems.</p>
      </div>
      <div class="service">
        <span class="service__label"><span class="service__icon"></span>Meditation for Wellness</span>
        <p>Personalized meditation for calm, healing and well-being.</p>
      </div>
      <p class="fee"><b>Fee Information:</b>Most major plans accepted and filed.</p>
    </div>
  </article>

  <article class="panel panel--back">
    <svg class="art" style="top:0" width="380" height="560" viewBox="0 0 380 560" role="img" aria-label="Photo of clear sparkling turquoise water">
      <defs><linearGradient id="water" x1="0" y1="0" x2="0" y2="1"><stop offset="0" stop-color="#3fb8d8"/><stop offset=".45" stop-color="#a9def0"/><stop offset=".7" stop-color="#fff"/></linearGradient></defs>
      <rect width="380" height="560" fill="url(#water)"/>
      <path d="M0 520 Q180 430 380 470" fill="none" stroke="var(--sky)" stroke-width="3"/>
    </svg>
    <div class="back">
      <div class="brand"><span class="brand__dot"></span>STILLWATER</div>
      <p class="doc-name">Maren Holloway, Psy.D.</p>
      <p class="back__role">Licensed Psychologist</p>
      <p class="back__motto">Heal the Past<br>Embrace the Present<br>Create the Future</p>
      <div class="contact">
        <div class="contact__row">
          <svg width="14" height="14" viewBox="0 0 14 14"><circle cx="7" cy="7" r="7" fill="var(--blue)"/><path d="M3.5 7.5 7 4l3.5 3.5V10.5h-7z" fill="#fff"/></svg>
          <b>Seaside Commons</b>410 Coral Way #12<br>Harbor Point, FL 30000
        </div>
        <div class="contact__row">
          <svg width="14" height="14" viewBox="0 0 14 14"><circle cx="7" cy="7" r="7" fill="var(--blue)"/><path d="M4.5 4c1 3 2.5 4.5 5.5 5.5l-1 1C6 9.5 4.5 8 3.5 5z" fill="#fff"/></svg>
          555 014-2290
        </div>
        <div class="contact__row">
          <svg width="14" height="14" viewBox="0 0 14 14"><circle cx="7" cy="7" r="7" fill="var(--blue)"/><circle cx="7" cy="7" r="3.6" fill="none" stroke="#fff"/><path d="M3.4 7h7.2M7 3.4v7.2" stroke="#fff"/></svg>
          www.stillwaterwc.com
        </div>
      </div>
    </div>
  </article>

  <article class="panel panel--cover">
    <svg class="art" style="top:0" width="380" height="560" viewBox="0 0 380 560" role="img" aria-label="Photo of a purple lotus flower on dark green water with lily pads">
      <defs>
        <radialGradient id="lotus" cx=".45" cy=".4" r=".6"><stop offset="0" stop-color="#9c7fe0"/><stop offset=".35" stop-color="#6b449b"/><stop offset=".7" stop-color="#4f8d33"/><stop offset="1" stop-color="#2d4d2c"/></radialGradient>
        <linearGradient id="meadow" x1="0" y1="0" x2="0" y2="1"><stop offset="0" stop-color="#fff"/><stop offset=".5" stop-color="#dcecb0"/><stop offset="1" stop-color="#7db43a"/></linearGradient>
      </defs>
      <rect width="380" height="560" fill="url(#meadow)"/>
      <path d="M0 0H380V190 Q200 300 0 250Z" fill="url(#lotus)"/>
      <path d="M0 258 Q200 310 380 196" fill="none" stroke="var(--sky)" stroke-width="4"/>
    </svg>
    <div class="cover">
      <div class="brand"><span class="brand__dot"></span>STILLWATER</div>
      <p class="doc-name">Maren Holloway, Psy.D.</p>
      <p class="cover__head">LIVE WELL, LOVE WELL<br><span>LICENSED PSYCHOLOGIST</span></p>
      <p class="cover__sub">Unleashing the Power of the Mind<br>for Healing and Well-being</p>
      <p class="script">Specializing in</p>
      <p class="cover__spec">Adults &amp; Harbor Lantern<br>Therapy</p>
      <p style="margin-top:8px"><span class="pill">
        <svg width="12" height="12" viewBox="0 0 14 14"><path d="M3 2c1.5 4.5 4 7 9 9l-1.5 1.8C5.5 11 3 8.5 1.2 3.5z" fill="#fff"/></svg>555 014-2290</span></p>
      <p class="url" style="margin-top:10px">www.stillwaterwc.com</p>
    </div>
  </article>
</section>

<!-- Inside spread -->
<section class="spread spread--inside">

  <article class="panel">
    <svg class="art" style="top:0" width="380" height="190" viewBox="0 0 380 190" role="img" aria-label="Photo of a dandelion seed head against a blue sky">
      <defs><radialGradient id="sky" cx=".4" cy=".5" r=".7"><stop offset="0" stop-color="#e8f2fb"/><stop offset=".4" stop-color="#5d95d6"/><stop offset="1" stop-color="#1c4f9c"/></radialGradient></defs>
      <path d="M0 0H300 Q340 110 230 175 Q120 200 0 165Z" fill="url(#sky)"/>
      <path d="M0 172 Q130 205 240 178" fill="none" stroke="var(--sky)" stroke-width="3"/>
    </svg>
    <div class="copy" style="top:200px">
      <h3 class="h">What is Harbor Lantern Therapy (HLT)</h3>
      <p>HLT dramatically enhances mood, creates calm, eases grief, optimizes health and promotes success. It is a form of hypnosis that clears stuck patterns of thinking and feeling at the subconscious level. Past emotionally charged memories are cleared. You do not have to talk about problems, share scattered thoughts, cry nor re-experience uncomfortable emotions. You are guided to engage in deep brain processing to create an internal shift for automatic changes in thoughts, feelings and behaviors. Profound change happens within your nervous system, facilitating lasting positive effects. Only one or two sessions are needed to experience immediate symptom relief.</p>
      <p style="font-weight:600;margin-bottom:4px">HLT is effective for many of life's problems including:</p>
      <ul class="ticks">
        <li><span class="tick"></span>PTSD, Sexual Abuse and Childhood Abuse</li>
        <li><span class="tick"></span>Grief, Infidelity and Heartbreak</li>
        <li><span class="tick"></span>Relationship Issues</li>
        <li><span class="tick"></span>Anger and Resentment</li>
        <li><span class="tick"></span>Guilt / Shame</li>
        <li><span class="tick"></span>Anxiety / Fear</li>
        <li><span class="tick"></span>Nightmares / Insomnia</li>
        <li><span class="tick"></span>Stress-related symptoms and Pain</li>
      </ul>
    </div>
  </article>

  <article class="panel panel--mist">
    <svg class="art" style="top:0" width="380" height="560" viewBox="0 0 380 560" aria-hidden="true">
      <path d="M380 400 Q320 470 345 560 H380Z" fill="#fff"/>
      <path d="M380 400 Q320 470 345 560" fill="none" stroke="var(--blue)" stroke-width="3"/>
    </svg>
    <div class="copy" style="top:28px;right:50px">
      <h3 class="h h--ink">Clearing old stuff and making way for new beginnings</h3>
      <p>If you have been unable to change how you feel, think or act, it is likely that you are being affected by experiences from your past. When something is painful or disturbing, it slams into awareness and leaves a lasting impression. Even when the experience is finished, deeper parts of the mind may continue to respond as if the disturbing event is still occurring. When fueled by the ongoing influence of past events, emotional problems and destructive behaviors may persist. You may consciously understand the value of changing a behavior, but unless your deeper mind is transformed, change is not likely. With HLT the subconscious mind is engaged, and the influence of past events is eliminated. Energy that was blocked is released and healing takes place. Negative habits and painful emotions are replaced by feelings of well-being and motivation for desired action.</p>
      <h3 class="h h--ink">What happens in an HLT Session?</h3>
      <p>Trauma is stored in the mind and body. In HLT, you will experience profound physiological calm and you will be guided towards emotional resolution in a gentle, creative and even humorous way. You access inner resources of light, wisdom and peace. You step into the awareness of your whole and true self. From this place of light, old memories are easily reframed with new meaning. You will leave the session feeling peaceful and sourced from within by a free-flowing energy.</p>
      <h3 class="h h--ink">Clear Your Mind and Change Your World</h3>
      <ul class="ticks" style="font-size:9.5px;line-height:1.6">
        <li><span class="tick"></span>Discover and resolve subconscious causes for emotional and behavioral difficulties</li>
        <li><span class="tick"></span>Eliminate unconscious conflicts blocking desired change</li>
        <li><span class="tick"></span>Promote mind / body healing</li>
      </ul>
      <p class="bio-url" style="margin-top:22px;text-align:center">www.stillwaterwc.com</p>
    </div>
  </article>

  <article class="panel">
    <div class="copy" style="top:28px">
      <h3 class="h" style="color:var(--blue)">Dr. Maren Holloway</h3>
      <p>Dr. Holloway is a licensed clinical psychologist specializing in adults and seniors. She treats people for depression, anxiety, grief, trauma, PTSD, relationship issues, infidelity, divorce and stress-related symptoms. She has over 20 years of clinical experience in mental health and is an adjunct counseling professor at a local university. She received her Master's and Doctorate degrees in Clinical Psychology and a Bachelor of Science degree in Rehabilitation. At Stillwater Wellness Center, she provides initial evaluations, assessment, diagnosis and comprehensive treatment planning. She will collaborate with you to create solutions for healing, empowerment and wellness.</p>
    </div>
    <div class="bio-contact">
      <div class="brand"><span class="brand__dot"></span>STILLWATER</div>
      <p class="bio-phone">&#9742; 555 014-2290</p>
      <p class="bio-url">www.stillwaterwc.com</p>
    </div>
    <svg class="art" style="top:290px" width="380" height="270" viewBox="0 0 380 270" role="img" aria-label="Portrait photo of the psychologist">
      <defs><linearGradient id="portrait" x1="0" y1="0" x2="1" y2="1"><stop offset="0" stop-color="#f1ece4"/><stop offset="1" stop-color="#c9b8a4"/></linearGradient></defs>
      <path d="M70 270 Q20 120 160 40 Q280 -10 380 40 V270Z" fill="url(#portrait)"/>
      <path d="M60 270 Q10 115 160 32 Q280 -20 380 32" fill="none" stroke="var(--sky)" stroke-width="4"/>
    </svg>
  </article>
</section>

</body>
</html>
```